Criação de Papelaria Profissional para Construção & Engenharia
" Nós extraimos o material e o beneficiamos em uma planta de britagem onde resulta no produto final utilizado para os diversos segmentos da construção civil e uso de um produto específico como remineralizador de solo voltado para agricultura "

```html
<!DOCTYPE html>
<html lang="pt-BR">
<head>
<meta charset="utf-8">
<title>Mineradora Serrano — Papelaria</title>
<link rel="stylesheet" href="https://fonts.googleapis.com/css2?family=Barlow:wght@400;500&display=swap">
<style>
  :root {
    --backdrop: #8d8b89;
    --paper: #f1f1f0;
    --paper-shade: #e6e6e5;
    --navy: #22336b;
    --navy-deep: #1b2a5c;
    --navy-flap: #2a3d7a;
    --gold: #c59a2e;
    --ink-light: #dfe3ee;
  }
  * { box-sizing: border-box; margin: 0; padding: 0; }
  html, body { width: 1200px; height: 1200px; overflow: hidden; }
  body {
    background: var(--backdrop);
    font-family: "Barlow", sans-serif;
    position: relative;
  }

  /* Card */
  .card {
    position: absolute;
    left: 120px; top: 290px;
    width: 660px; height: 330px;
    background: linear-gradient(135deg, var(--paper) 0%, var(--paper-shade) 100%);
    box-shadow: 0 6px 18px rgba(0,0,0,.18);
  }
  .card__strip {
    position: absolute; left: 0; right: 0; bottom: 0;
    height: 9px; background: var(--gold);
  }
  .brand {
    position: absolute;
    display: flex; align-items: center; gap: 12px;
  }
  .brand__mark { width: 18px; height: 18px; background: var(--gold); flex: none; }
  .brand__name {
    font-weight: 500; letter-spacing: .5px; line-height: 1.02;
    text-transform: uppercase;
  }
  .card .brand { left: 28px; top: 96px; }
  .card .brand__name { color: var(--navy); font-size: 29px; }

  /* Envelope */
  .envelope {
    position: absolute;
    left: 420px; top: 680px;
    width: 660px; height: 330px;
    background: var(--navy);
    box-shadow: 0 6px 18px rgba(0,0,0,.22);
    overflow: hidden;
  }
  .envelope__texture {
    position: absolute; inset: 0;
    background: linear-gradient(120deg, var(--navy) 0%, var(--navy-deep) 60%, var(--navy) 100%);
  }
  .envelope__flap {
    position: absolute; right: 0; top: 0; width: 120px; height: 321px;
  }
  .envelope__strip {
    position: absolute; left: 0; right: 0; bottom: 0;
    height: 9px; background: var(--gold);
  }
  .envelope .brand { left: 40px; top: 238px; gap: 9px; }
  .envelope .brand__mark { width: 12px; height: 12px; }
  .envelope .brand__name { color: #ffffff; font-size: 15px; }

  .contacts {
    position: absolute; left: 168px; top: 238px;
    list-style: none;
    display: flex; flex-direction: column; gap: 7px;
  }
  .contacts li {
    display: flex; align-items: center; gap: 6px;
    color: var(--ink-light); font-size: 8.5px; line-height: 11px;
    white-space: nowrap;
  }
  .contacts svg { width: 10px; height: 10px; flex: none; }
  .contacts .web { font-weight: 500; color: #ffffff; }

  .address {
    position: absolute; left: 356px; top: 255px;
    font-style: normal; color: var(--ink-light);
    font-size: 8.5px; line-height: 18px;
    white-space: nowrap;
  }
</style>
</head>
<body>

  <section class="card">
    <div class="brand">
      <span class="brand__mark"></span>
      <span class="brand__name">Mineradora<br>Serrano</span>
    </div>
    <div class="card__strip"></div>
  </section>

  <section class="envelope">
    <div class="envelope__texture" role="img" aria-label="Fine diagonal line pattern in navy tones"></div>
    <svg class="envelope__flap" viewBox="0 0 120 321" preserveAspectRatio="none" aria-hidden="true">
      <path d="M0 0 L120 0 L120 321 L20 321 Q4 160 0 0 Z" fill="var(--navy-flap)"/>
    </svg>

    <div class="brand">
      <span class="brand__mark"></span>
      <span class="brand__name">Mineradora<br>Serrano</span>
    </div>

    <ul class="contacts">
      <li>
        <svg viewBox="0 0 12 12"><circle cx="6" cy="6" r="6" fill="var(--gold)"/><path d="M4 3.2 L5 3 L5.6 4.6 L5 5.1 Q5.6 6.4 6.9 7 L7.4 6.4 L9 7 L8.8 8 Q6.8 8.4 5.2 6.8 Q3.6 5.2 4 3.2Z" fill="var(--navy)"/></svg>
        21 04400-0011
      </li>
      <li>
        <svg viewBox="0 0 12 12"><circle cx="6" cy="6" r="6" fill="var(--gold)"/><rect x="3" y="4" width="6" height="4.2" fill="none" stroke="var(--navy)" stroke-width=".9"/><path d="M3 4 L6 6.4 L9 4" fill="none" stroke="var(--navy)" stroke-width=".9"/></svg>
        contato@mineradoraserrano.com
      </li>
      <li class="web">
        <svg viewBox="0 0 12 12"><circle cx="6" cy="6" r="6" fill="var(--gold)"/><circle cx="6" cy="6" r="3" fill="none" stroke="var(--navy)" stroke-width=".9"/><path d="M3 6 H9 M6 3 V9" stroke="var(--navy)" stroke-width=".8"/></svg>
        mineradoraserrano.com
      </li>
    </ul>

    <address class="address">
      Rua das Pedras, 240<br>
      Centro, Cidade Nova - RJ
    </address>

    <div class="envelope__strip"></div>
  </section>

</body>
</html>
```